Aviation club power point template

Hello designers
we are a small aviation club with about 100 members in germany. we love flying and are looking for a professional power point template for our public relations.
Here is the link to our homepage
https://www.lgk-tarnbach.de/
the template should be aviation related and should be about gliders and small powered aircraft.
Here you can find our gliders (you see the right link only in german language)
https://www.lgk-tarnbach.de/flying/gliding/
Here you can find our motor planes (Only Falke KV-250) (you see the right link only in German language)
https://www.lgk-tarnbach.de/flying/motorflying/
I found a model of the Falke KV-250 motor plane, but in green. We have a red-white painting
http://www.zulmodels.com/wp-content/uploads/Image10-300x198. png
Required foils:
3 welcome (one neutral, one glider, one powered plane)
1-2 agenda
2-3 statistics
2-3 enumerations
2-3 free slides
We look forward to your suggestions and thank you in advance for your work. If you have any questions or need more data. Please write us.
greetings
jonas

```html
<!DOCTYPE html>
<html lang="de">
<head>
<meta charset="utf-8">
<title>Luftsportgruppe Tarnbach – Präsentationsvorlage</title>
<link href="https://fonts.googleapis.com/css2?family=Arimo:wght@400;700&family=Montserrat:wght@400;600;700&display=swap" rel="stylesheet">
<style>
  :root {
    --navy: #1b2a5e;
    --navy-deep: #16224f;
    --teal: #2bb8ae;
    --page: #f3f4f6;
    --ink: #4a4a4a;
    --rule: #d9dce4;
    --white: #ffffff;
  }
  * { box-sizing: border-box; margin: 0; padding: 0; }
  html, body { width: 1200px; height: 4161px; overflow: hidden; background: var(--page); }
  body { position: relative; font-family: "Arimo", Arial, sans-serif; color: var(--ink); }

  .slide {
    position: absolute; left: 52px; width: 1096px; height: 618px;
    background: var(--white); overflow: hidden;
    box-shadow: 0 2px 6px rgba(20, 30, 60, 0.12);
  }
  .slide--welcome { top: 70px; }
  .slide--agenda { top: 746px; }
  .slide--stats { top: 1438px; }
  .slide--list { top: 2128px; }
  .slide--free { top: 2810px; }
  .slide--thanks { top: 3466px; background: var(--navy); }

  .photo { position: absolute; }

  /* club name mark */
  .club-mark { position: absolute; display: flex; align-items: center; gap: 8px; color: var(--navy); font-weight: 700; }
  .club-mark__dot { border: 3px solid currentColor; border-radius: 50%; flex: none; }
  .club-mark__name { line-height: 1.25; }

  /* welcome */
  .welcome__photo { inset: 0; background: linear-gradient(100deg, #1f3478 0%, #2c4f9e 35%, #6f95cf 60%, #b8cde8 78%, #5b6f96 100%); }
  .welcome__peaks { position: absolute; left: 0; right: 0; bottom: 0; height: 190px; background: linear-gradient(180deg, rgba(210,222,240,0) 0%, rgba(60,76,120,0.55) 55%, #22305e 100%); }
  .welcome__mark { left: 50px; top: 90px; color: var(--white); font-size: 15px; }
  .welcome__title { position: absolute; left: 50px; top: 310px; font-family: "Montserrat", Arial, sans-serif; font-weight: 700; font-size: 21px; color: var(--white); letter-spacing: 0.3px; }
  .welcome__text { position: absolute; left: 50px; top: 360px; width: 430px; font-family: "Montserrat", Arial, sans-serif; font-size: 15px; line-height: 27px; color: var(--white); }

  /* agenda */
  .agenda__panel { position: absolute; left: 0; top: 0; width: 236px; height: 100%; background: var(--navy); }
  .agenda__hint { position: absolute; left: 33px; top: 32px; color: var(--white); font-size: 11.5px; }
  .agenda__title { position: absolute; left: 39px; top: 290px; color: var(--white); font-size: 36px; font-weight: 700; }
  .agenda__photo { left: 236px; top: 0; width: 326px; height: 100%; background: linear-gradient(180deg, #7d92b4 0%, #a9b9d0 35%, #c8d4e4 60%, #8d9fbb 80%, #e6ecf4 100%); }
  .agenda__list { position: absolute; left: 548px; top: 120px; width: 514px; list-style: none; }
  .agenda__item { position: relative; height: 68px; }
  .agenda__tab { position: absolute; left: 0; top: 6px; width: 52px; height: 44px; background: var(--navy); border-radius: 0 22px 22px 0; }
  .agenda__tab svg { position: absolute; left: 16px; top: 12px; }
  .agenda__label { position: absolute; left: 92px; top: 18px; font-size: 18px; font-weight: 700; color: var(--navy); letter-spacing: 0.3px; }
  .agenda__rule { position: absolute; left: 92px; right: 0; top: 58px; height: 1px; background: var(--rule); }

  /* shared slide header */
  .slide-head { position: absolute; }
  .slide-head::before { content: ""; display: block; width: 44px; height: 3px; background: var(--navy); margin-bottom: 12px; }
  .slide-head__title { font-size: 25px; color: var(--navy); font-weight: 400; letter-spacing: 0.2px; }
  .slide-head__sub { font-size: 11.5px; color: #555; margin-top: 6px; }
  .corner-mark { right: 24px; top: 20px; font-size: 11px; width: 150px; }

  .body-text { position: absolute; font-size: 12.5px; line-height: 24px; text-align: justify; color: var(--ink); }
  .body-text p + p { margin-top: 22px; }

  .chart { position: absolute; left: 40px; top: 150px; }
  .chart text { font-family: "Arimo", Arial, sans-serif; font-size: 7px; fill: #333; }

  /* list slide */
  .list__photo { position: absolute; left: 0; top: 0; }

  /* free slide */
  .free__mark { left: 70px; top: 150px; font-size: 30px; gap: 18px; width: 380px; }

  /* thanks */
  .thanks__mark { position: absolute; left: 50%; top: 50%; width: 420px; height: 420px; margin: -210px 0 0 -210px; border: 18px solid rgba(255,255,255,0.05); border-radius: 50%; display: flex; align-items: flex-end; justify-content: center; padding-bottom: 40px; font-size: 30px; font-weight: 700; color: rgba(255,255,255,0.06); }
  .thanks__title { position: absolute; left: 0; right: 0; top: 238px; text-align: center; font-size: 104px; font-weight: 700; color: var(--white); letter-spacing: 2px; }
</style>
</head>
<body>

<section class="slide slide--welcome">
  <div class="photo welcome__photo" role="img" aria-label="Segelflugzeug im Flug über verschneiten Berggipfeln unter blauem Himmel"></div>
  <div class="welcome__peaks"></div>
  <div class="club-mark welcome__mark">
    <span class="club-mark__dot" style="width:26px;height:26px"></span>
    <span class="club-mark__name">Luftsportgruppe<br>Tarnbach e.V.</span>
  </div>
  <h1 class="welcome__title">HERZLICH WILLKOMMEN</h1>
  <p class="welcome__text">Aber damit Sie sehen, woher all dieser angeborene Irrtum derer kommt, die Vergnügen anklagen und Schmerz preisen, werde ich die ganze</p>
</section>

<section class="slide slide--agenda">
  <div class="agenda__panel">
    <p class="agenda__hint">Fügen Sie hier Ihren Text hinzu</p>
    <h2 class="agenda__title">AGENDA</h2>
  </div>
  <div class="photo agenda__photo" role="img" aria-label="Segelflugzeug vor Wolken über schneebedeckten Bergen"></div>
  <ul class="agenda__list">
    <li class="agenda__item"><span class="agenda__tab"><svg width="20" height="20" viewBox="0 0 20 20"><circle cx="10" cy="10" r="8" fill="none" stroke="#fff" stroke-width="1"/><path d="M8.5 6.5 L12 10 L8.5 13.5" fill="none" stroke="#fff" stroke-width="1.2"/></svg></span><span class="agenda__label">EINFÜHRUNG</span><span class="agenda__rule"></span></li>
    <li class="agenda__item"><span class="agenda__tab"><svg width="20" height="20" viewBox="0 0 20 20"><circle cx="10" cy="10" r="8" fill="none" stroke="#fff" stroke-width="1"/><path d="M8.5 6.5 L12 10 L8.5 13.5" fill="none" stroke="#fff" stroke-width="1.2"/></svg></span><span class="agenda__label">AGENDA</span><span class="agenda__rule"></span></li>
    <li class="agenda__item"><span class="agenda__tab"><svg width="20" height="20" viewBox="0 0 20 20"><circle cx="10" cy="10" r="8" fill="none" stroke="#fff" stroke-width="1"/><path d="M8.5 6.5 L12 10 L8.5 13.5" fill="none" stroke="#fff" stroke-width="1.2"/></svg></span><span class="agenda__label">STATISTIKEN</span><span class="agenda__rule"></span></li>
    <li class="agenda__item"><span class="agenda__tab"><svg width="20" height="20" viewBox="0 0 20 20"><circle cx="10" cy="10" r="8" fill="none" stroke="#fff" stroke-width="1"/><path d="M8.5 6.5 L12 10 L8.5 13.5" fill="none" stroke="#fff" stroke-width="1.2"/></svg></span><span class="agenda__label">AUFZÄHLUNGEN</span><span class="agenda__rule"></span></li>
    <li class="agenda__item"><span class="agenda__tab"><svg width="20" height="20" viewBox="0 0 20 20"><circle cx="10" cy="10" r="8" fill="none" stroke="#fff" stroke-width="1"/><path d="M8.5 6.5 L12 10 L8.5 13.5" fill="none" stroke="#fff" stroke-width="1.2"/></svg></span><span class="agenda__label">KOSTENLOSE FOLIEN</span><span class="agenda__rule"></span></li>
    <li class="agenda__item"><span class="agenda__tab"><svg width="20" height="20" viewBox="0 0 20 20"><circle cx="10" cy="10" r="8" fill="none" stroke="#fff" stroke-width="1"/><path d="M8.5 6.5 L12 10 L8.5 13.5" fill="none" stroke="#fff" stroke-width="1.2"/></svg></span><span class="agenda__label">KONTAKTIERE UNS</span><span class="agenda__rule"></span></li>
  </ul>
</section>

<section class="slide slide--stats">
  <header class="slide-head" style="left:16px;top:28px">
    <h2 class="slide-head__title">STATISTIKEN</h2>
    <p class="slide-head__sub">UNTERTITEL GEHT HIER</p>
  </header>
  <div class="club-mark corner-mark"><span class="club-mark__dot" style="width:18px;height:18px"></span><span class="club-mark__name">Luftsportgruppe Tarnbach e.V.</span></div>
  <svg class="chart" width="640" height="340" viewBox="0 0 640 340">
    <g stroke="#e3e6ec" stroke-width="1">
      <line x1="0" y1="28" x2="630" y2="28"/><line x1="0" y1="100" x2="630" y2="100"/>
      <line x1="0" y1="172" x2="630" y2="172"/><line x1="0" y1="244" x2="630" y2="244"/>
      <line x1="0" y1="315" x2="630" y2="315"/>
    </g>
    <g text-anchor="middle">
      <rect x="24" y="98" width="22" height="217" fill="#1b2a5e"/><text x="35" y="92">46.65%</text><text x="35" y="330">JAN 2012</text>
      <rect x="85" y="165" width="22" height="150" fill="#2bb8ae"/><text x="96" y="159">32.26%</text><text x="96" y="330">FEB 2013</text>
      <rect x="145" y="123" width="22" height="192" fill="#1b2a5e"/><text x="156" y="117">41.25%</text><text x="156" y="330">MAR 2014</text>
      <rect x="206" y="268" width="22" height="47" fill="#2bb8ae"/><text x="217" y="262">10.03%</text><text x="217" y="330">APR 2015</text>
      <rect x="266" y="237" width="22" height="78" fill="#1b2a5e"/><text x="277" y="231">16.79%</text><text x="277" y="330">MAY2016</text>
      <rect x="327" y="41" width="22" height="274" fill="#2bb8ae"/><text x="338" y="35">58.98%</text><text x="338" y="330">JUN 2017</text>
      <rect x="387" y="160" width="22" height="155" fill="#1b2a5e"/><text x="398" y="154">33.42%</text><text x="398" y="330">JUL 2018</text>
      <rect x="448" y="251" width="22" height="64" fill="#2bb8ae"/><text x="459" y="245">13.73%</text><text x="459" y="330">AUG 2019</text>
      <rect x="508" y="202" width="22" height="113" fill="#1b2a5e"/><text x="519" y="196">24.30%</text><text x="519" y="330">SEP 2020</text>
      <rect x="569" y="163" width="22" height="152" fill="#2bb8ae"/><text x="580" y="157">32.67%</text><text x="580" y="330">OCT 2021</text>
    </g>
  </svg>
  <div class="body-text" style="left:672px;top:136px;width:400px">
    <p>Aber damit Sie sehen, woher all dieser angeborene Irrtum derer kommt, die Vergnügen anklagen und Schmerz preisen, werde ich die ganze Sache öffnen und genau das erklären, was dieser Entdecker der Wahrheit und sozusagen der Architekt der Wahrheit gesagt hat ein glückliches Leben. Denn niemand ver achtet oder hasst oder läuft vor Vergnügen davon, weil es Vergnügen ist, sondern weil große Schmerzen für diejenigen entstehen, die nicht wissen, wie man Vergnügen mit Vernunft folgt.</p>
    <p>Auch gibt es niemanden, der, weil er den Schmerz liebt, ihm nachj agt, ihn gewinnen will, aber weil es nie solche Zeiten gibt, in denen er durch Arbeit und Schmerz ein großes Vergnügen sucht. Denn um ins kleinste Detail zu kommen, keiner von uns unternimmt eine mühs elige Körperübung, es sei denn, um daraus einen Nutzen zu ziehen.</p>
    <p>Denn niemand verachtet oder hasst oder läuft vor Vergnügen davon, weil es Vergnügen ist, sondern weil große Schmerzen für diejenigen nicht wissen, wie man Vergnügen mit Vernunft folgt.</p>
  </div>
</section>

<section class="slide slide--list">
  <svg class="list__photo" width="1096" height="618" viewBox="0 0 1096 618" role="img" aria-label="Vereinsmitglieder versammelt auf einer Wiese vor dem Vereinsheim">
    <defs><linearGradient id="field" x1="0" y1="0" x2="0" y2="1"><stop offset="0" stop-color="#9fc0e2"/><stop offset="0.22" stop-color="#4f6a3a"/><stop offset="0.45" stop-color="#7a6a5c"/><stop offset="0.62" stop-color="#3f5a32"/><stop offset="1" stop-color="#4e8a2c"/></linearGradient></defs>
    <polygon points="640,0 1096,0 1096,618 420,618" fill="url(#field)"/>
  </svg>
  <header class="slide-head" style="left:32px;top:24px">
    <h2 class="slide-head__title">AUFZÄHLUNGEN</h2>
    <p class="slide-head__sub">UNTERTITEL GEHT HIER</p>
  </header>
  <div class="club-mark corner-mark" style="color:#fff"><span class="club-mark__dot" style="width:18px;height:18px"></span><span class="club-mark__name">Luftsportgruppe Tarnbach e.V.</span></div>
  <div class="body-text" style="left:46px;top:128px;width:395px;line-height:22px;font-size:12px">
    <p>Aber damit Sie sehen, woher all dieser angeborene Irrtum kommt, jetzt klagen sie Lust und jetzt Schmerz und jetzt Lob an, werde ich die ganze Sache aufdecken, und ich werde genau die Dinge erkl ären, die von diesem Entdecker der Wahrheit gesagt wurden und , sozusagen der Architekt eines glücklichen Lebens. Denn niemand verachtet, hasst oder flieht vor dem Vergnügen selbst, weil es Vergnügen ist, sondern weil große Schmerzen von denen her- rühren, die nicht wissen, wie man dem Vergnügen folgt. Auch gibt es niemanden, der Schmerz erlangen will, weil es Schmerz ist, sondern weil er durch Arbeit und Schmerz ein großes Vergnügen sucht.Aber ich muss Ihnen erklären, wie all diese irrige Vorstellung,</p>
    <p>Freude anzuprangern und Schmerz zu preisen, entstanden ist, und ich werde Ihnen einen vollständigen Bericht über das System geben und die tatsächlichen Lehren des großen Erforschers der Wahrheit, des Baumeisters, darlegen des menschlichen Glücks. Selbst diej enigen, die nicht wissen, wie man Vergnügen rat ional verfolgt, stoßen auf extrem schmerzhafte Folgen.</p>
  </div>
</section>

<section class="slide slide--free">
  <header class="slide-head" style="left:32px;top:24px">
    <h2 class="slide-head__title">KOSTENLOSE FOLIEN</h2>
    <p class="slide-head__sub">UNTERTITEL GEHT HIER</p>
  </header>
  <div class="club-mark corner-mark"><span class="club-mark__dot" style="width:18px;height:18px"></span><span class="club-mark__name">Luftsportgruppe Tarnbach e.V.</span></div>
  <div class="club-mark free__mark"><span class="club-mark__dot" style="width:60px;height:60px;border-width:5px"></span><span class="club-mark__name">Luftsportgruppe<br>Tarnbach e.V.</span></div>
  <div class="body-text" style="left:474px;top:186px;width:548px;font-size:12px;line-height:22px">
    <p>Aber damit Sie sehen, woher all dieser angeborene Irrtum kommt, jetzt klagen sie Lust und jetzt Schmerz und jetzt Lob an, werde ich die ganze Sache aufdecken, und ich werde genau die Dinge erkl ären, die von diesem Entdecker der Wahrheit gesagt wurden und , sozusagen der Architekt eines glücklichen Lebens. Denn niemand verachtet, hasst oder flieht vor dem Vergnüg en selbst, weil es Vergnügen ist, sondern weil große Schmerzen von denen herr ühren, die nicht wissen, wie man dem Vergnügen folgt. Auch gibt es niemanden, der Schmerz erlangen will, weil es Schmerz ist, sondern weil er durch Arbeit und Schmerz ein großes Vergnügen sucht.Aber ich muss Ihnen erklären, wie all diese irrige Vorstellung,</p>
    <p style="margin-top:18px">Freude anzuprangern und Schmerz zu preisen, entstanden ist, und ich werde Ihnen einen volls tändigen Bericht über das System geben und die tatsächlichen Lehren des großen Erforschers der Wahrheit, des Baumeisters, darlegen des menschlichen Glücks. Selbst diej enigen, die nicht wissen, wie man Vergnügen rat ional verfolgt, stoßen auf extrem schmerzhafte Folgen.</p>
  </div>
</section>

<section class="slide slide--thanks">
  <div class="thanks__mark">Luftsportgruppe Tarnbach e.V.</div>
  <h2 class="thanks__title">DANKE</h2>
</section>

</body>
</html>
```